'Lanterns' CD cover project

I am recording a new album 'Lanterns' and need a CD cover design. No design specs, but I want something simple and classy. My name (Marek Townley) does not necessarily have to appear on the cover, and it does not have to relate to my previous 11 albums. I have posted some of my own ideas on Snapwall.

Target Market(s)

I have an established 50s+ fan base, but am seeking to appeal to a younger more modern audience.

Font styles to use
Other font styles liked:
• Yu Gothic Light but open to suggestions.

Colors

Designer to choose colors to be used in the design.

Requirements
Must have
• Simple, clean, classy, Im open to a photo image or simply a graphic design.
Nice to have
• Modern (pastel?) colors.. if pastels are modern?!
Should not have
• Nothing 'In Yer Face'. Prefer sublte, nuance, classy, tasteful, clean lines, unusual font.

```html
<!DOCTYPE html>
<html lang="en">
<head>
<meta charset="utf-8">
<title>Lanterns — Marek Townley</title>
<link rel="stylesheet" href="https://fonts.googleapis.com/css2?family=Montserrat:wght@300;400&display=swap">
<style>
  :root {
    --page-bg: #f1f1f1;
    --rock-dark: #1f1f22;
    --rock-mid: #3a3836;
    --rock-light: #5d5853;
    --water-mist: #9aa3a6;
    --water-deep: #2f4245;
    --type-white: #f4f4f2;
  }
  * { margin: 0; padding: 0; box-sizing: border-box; }
  html, body {
    width: 1200px;
    height: 1000px;
    overflow: hidden;
    background: var(--page-bg);
  }
  .album-cover {
    position: absolute;
    left: 200px;
    top: 100px;
    width: 800px;
    height: 800px;
    overflow: hidden;
  }
  .cover-photo {
    position: absolute;
    inset: 0;
    background:
      radial-gradient(ellipse 22% 45% at 62% 75%, var(--water-mist) 0%, rgba(154,163,166,0.35) 45%, transparent 75%),
      radial-gradient(ellipse 18% 25% at 70% 40%, rgba(120,128,130,0.55) 0%, transparent 70%),
      radial-gradient(ellipse 30% 20% at 55% 95%, var(--water-deep) 0%, transparent 80%),
      radial-gradient(ellipse 40% 60% at 20% 55%, var(--rock-light) 0%, transparent 70%),
      radial-gradient(ellipse 25% 50% at 88% 70%, var(--rock-light) 0%, transparent 75%),
      linear-gradient(180deg, var(--rock-dark) 0%, var(--rock-mid) 55%, var(--rock-dark) 100%);
  }
  .cover-title {
    position: absolute;
    left: 50%;
    top: 346px;
    transform: translateX(-50%);
    height: 73px;
    padding: 0 26px 0 40px;
    border: 2px solid var(--type-white);
    display: flex;
    align-items: center;
    font-family: "Montserrat", sans-serif;
    font-weight: 300;
    font-size: 34px;
    letter-spacing: 0.62em;
    color: var(--type-white);
    white-space: nowrap;
  }
  .cover-artist {
    position: absolute;
    left: 0;
    right: 0;
    top: 700px;
    text-align: center;
    padding-left: 0.55em;
    font-family: "Montserrat", sans-serif;
    font-weight: 400;
    font-size: 21px;
    letter-spacing: 0.55em;
    color: var(--type-white);
  }
</style>
</head>
<body>
  <main class="album-cover">
    <div class="cover-photo" role="img" aria-label="Photograph of a misty river rushing through a narrow dark rock gorge"></div>
    <h1 class="cover-title">LANTERNS</h1>
    <p class="cover-artist">MAREK TOWNLEY</p>
  </main>
</body>
</html>
```